Design Box Packaging with Logo for a high-end menswear store

I would like to come up with a design for our shipping boxes.
- Printing would only be in 1 colour. (box will be in mid beige/brown)
- I want it to look modern and clean
- I have attached my logo
- It is for a high-end menswear store for shipping clothing for online purchases
Size of the box is about 14 x 10 x 5

Target Market(s)

High-end / wealthy people shopping online

Industry/Entity Type

Clothing, retail, online high-end clothing

Colors

Designer to choose colors to be used in the design.

Requirements
Must have
• Look sharp and clean, have logo information, online printing one colour
Nice to have
• Look clean and modern

```html
<!DOCTYPE html>
<html lang="en">
<head>
<meta charset="utf-8">
<title>Shipping Box Print – Maison Corbel</title>
<link rel="stylesheet" href="https://fonts.googleapis.com/css2?family=Rye&family=Roboto+Slab:wght@700&display=swap">
<style>
  :root {
    --page: #efefef;
    --kraft: #e4cdb0;
    --ink: #1d1b19;
    --fold: #c9b293;
  }
  * { margin: 0; padding: 0; box-sizing: border-box; }
  html, body { width: 1200px; height: 1080px; overflow: hidden; background: var(--page); }
  .canvas { position: relative; width: 1200px; height: 1080px; }

  .panel { position: absolute; background: var(--kraft); outline: 1px dashed var(--fold); overflow: hidden; }
  .panel--end { left: 125px; top: 120px; width: 250px; height: 500px; }
  .panel--lid { left: 375px; top: 120px; width: 700px; height: 500px; }
  .panel--front { left: 375px; top: 620px; width: 700px; height: 250px; }

  .display { font-family: "Rye", serif; letter-spacing: 4px; }
  .slab { font-family: "Roboto Slab", serif; font-weight: 700; }

  .lid-band {
    position: absolute; left: 0; top: 0; width: 100%; height: 130px;
    background: var(--ink); color: var(--kraft);
    display: flex; align-items: center; justify-content: center;
    font-size: 104px;
  }

  .brand { display: flex; align-items: center; gap: 12px; color: var(--ink); position: absolute; }
  .brand__square { width: 34px; height: 34px; background: var(--ink); }
  .brand__name { font-size: 26px; letter-spacing: 1px; }
  .panel--lid .brand { left: 90px; top: 300px; }
  .panel--front .brand { right: 40px; top: 36px; }
  .panel--front .brand__name { font-size: 22px; }
  .panel--front .brand__square { width: 28px; height: 28px; }

  .gent-art { position: absolute; background: linear-gradient(180deg, #d6bd9c, #cbb190); border-radius: 6px; }
  .panel--lid .gent-art { right: 90px; top: 200px; width: 150px; height: 230px; }
  .panel--front .gent-art { left: 60px; top: 24px; width: 84px; height: 130px; }

  .front-title { position: absolute; left: 175px; top: 60px; font-size: 54px; color: var(--ink); }

  .front-band {
    position: absolute; left: 0; bottom: 0; width: 100%; height: 70px;
    background: var(--ink); color: var(--kraft);
    display: flex; align-items: center; justify-content: center;
    font-size: 30px; letter-spacing: 2px; gap: 22px;
  }
  .front-band__rule { width: 3px; height: 34px; background: var(--kraft); }

  .end-label {
    position: absolute; left: 50%; top: 50%;
    transform: translate(-50%, -50%) rotate(90deg);
    font-family: "Roboto Slab", serif; font-weight: 700;
    font-size: 40px; letter-spacing: 6px; color: var(--ink); white-space: nowrap;
  }
</style>
</head>
<body>
<main class="canvas">
  <section class="panel panel--end">
    <p class="end-label">FOR MEN</p>
  </section>

  <section class="panel panel--lid">
    <h1 class="lid-band display">FASHION</h1>
    <div class="brand">
      <span class="brand__square"></span>
      <span class="brand__name slab">Maison Corbel</span>
    </div>
    <div class="gent-art" role="img" aria-label="Line illustration of a gentleman's bowler hat, round glasses, moustache and bow tie"></div>
  </section>

  <section class="panel panel--front">
    <div class="gent-art" role="img" aria-label="Small illustration of a bowler hat, round glasses, moustache and bow tie"></div>
    <h2 class="front-title display">FASHION</h2>
    <div class="brand">
      <span class="brand__square"></span>
      <span class="brand__name slab">Maison Corbel</span>
    </div>
    <p class="front-band slab">MEN'S CLOTHES <span class="front-band__rule"></span> MEN'S FASHION</p>
  </section>
</main>
</body>
</html>
```